Appointments cards for my business "Brightpath wellness clinic"

I need an appointment card for my business, I will attach the current business card, the logo its self will stay the same, I will attach my most recent personal business card as well. Im looking for a cross in-between both cards not to fancy though.
the back of the card will have the appointment date and time on it... But I don't want my photo on these appointment cards. thank you

Target Market(s)

25-50 year old

Industry/Entity Type

Health Care

Contact Information for Business Card

Brightpath Wellness & Vitality clinic
1746 birch ave ste#2
sounth ogden ut 84312
phone# (801) 555-0142
fax# (801)555-0143
brightpathwellclinic.example

Font styles to use
Serif
Sans Serif
Script

Colors

Designer to choose colors to be used in the design.

Requirements
Must have
• the logo the address ...info
Nice to have
• I would like to mix my new card with logo and my business card
Should not have
• see above

```html
<!DOCTYPE html>
<html lang="en">
<head>
<meta charset="utf-8">
<title>Brightpath Wellness Clinic – Appointment Card</title>
<link href="https://fonts.googleapis.com/css2?family=Lora:wght@400;700&display=swap" rel="stylesheet">
<style>
  :root {
    --stage: #2b2b2d;
    --sky-light: #f4f9fd;
    --sky: #c9e2f2;
    --copper-light: #c46a3a;
    --copper: #a24e26;
    --ink: #1d1d1f;
    --rule: #5d6a74;
    --cream: #fbeee2;
    --shadow: #0d0d0e;
  }
  * { box-sizing: border-box; margin: 0; padding: 0; }
  html, body {
    width: 1200px; height: 880px; overflow: hidden;
    background: var(--stage);
    font-family: "Lora", Georgia, serif;
    color: var(--ink);
  }
  .card {
    position: absolute; left: 250px;
    width: 700px; height: 400px;
    overflow: hidden;
    box-shadow: 0 8px 24px rgba(0,0,0,.45);
  }
  .card--front { top: 26px; }
  .card--back { top: 454px; }
  .card__bg { position: absolute; inset: 0; width: 100%; height: 100%; }

  /* front */
  .brand-name {
    position: absolute; left: 20px; top: 96px; width: 140px;
    font-size: 17px; font-weight: 700; line-height: 1.25;
    color: var(--cream); text-transform: uppercase; letter-spacing: .5px;
  }
  .contact {
    position: absolute; left: 240px; top: 100px; width: 440px;
    text-align: center; font-size: 25px; line-height: 1.3;
  }
  .contact__line--gap { margin-top: 14px; }
  .contact__label { font-weight: 700; }
  .contact__web { margin-top: 18px; }

  /* back */
  .appt { position: absolute; inset: 0; }
  .appt__rule {
    position: absolute; left: 80px; right: 70px; top: 62px;
    border-top: 1.5px solid var(--rule);
  }
  .appt__title {
    position: absolute; top: 82px; left: 0; right: 0;
    text-align: center; font-size: 31px; font-weight: 400;
  }
  .days {
    position: absolute; top: 160px; left: 60px; right: 50px;
    display: flex; justify-content: space-between; list-style: none;
  }
  .day { display: flex; align-items: center; gap: 14px; font-size: 19px; }
  .day__box {
    width: 30px; height: 28px; background: #fff;
    border: 1.5px solid #8a9aa6;
  }
  .when {
    position: absolute; top: 222px; left: 60px; right: 50px;
    display: flex; align-items: flex-end; gap: 14px; font-size: 22px;
  }
  .when__line { flex: 1; border-bottom: 1.5px solid var(--rule); margin-bottom: 6px; }
  .when__line--date { flex: 1.35; }
  .when__meridiem { font-size: 18px; line-height: 1.05; }
  .appt__web {
    position: absolute; top: 318px; left: 0; right: 0;
    text-align: center; font-size: 21px;
  }
</style>
</head>
<body>

<section class="card card--front" aria-label="Card front">
  <svg class="card__bg" viewBox="0 0 700 400" aria-hidden="true">
    <defs>
      <linearGradient id="copperFront" x1="0" y1="0" x2="0" y2="1">
        <stop offset="0" stop-color="var(--copper)"/>
        <stop offset="1" stop-color="var(--copper-light)"/>
      </linearGradient>
      <radialGradient id="skyFront" cx=".6" cy=".5" r=".6">
        <stop offset="0" stop-color="var(--sky-light)"/>
        <stop offset="1" stop-color="var(--sky)"/>
      </radialGradient>
    </defs>
    <rect width="700" height="400" fill="url(#copperFront)"/>
    <circle cx="510" cy="220" r="362" fill="var(--shadow)"/>
    <circle cx="530" cy="230" r="360" fill="url(#skyFront)"/>
  </svg>
  <div class="brand-name">Brightpath Wellness &amp; Vitality Clinic</div>
  <div class="contact">
    <p>1746 Birch Ave ste#2</p>
    <p>Fernhollow Westmark 84312</p>
    <p class="contact__line--gap"><span class="contact__label">P:</span> 1(555)555-0142</p>
    <p><span class="contact__label">F:</span> 555-555-0143</p>
    <p class="contact__web">www.brightpathwellclinic.example</p>
  </div>
</section>

<section class="card card--back" aria-label="Card back">
  <svg class="card__bg" viewBox="0 0 700 400" aria-hidden="true">
    <defs>
      <linearGradient id="copperBack" x1="0" y1="0" x2="1" y2="1">
        <stop offset="0" stop-color="var(--copper)"/>
        <stop offset="1" stop-color="var(--copper-light)"/>
      </linearGradient>
      <radialGradient id="skyBack" cx=".5" cy=".35" r=".65">
        <stop offset="0" stop-color="var(--sky-light)"/>
        <stop offset="1" stop-color="var(--sky)"/>
      </radialGradient>
    </defs>
    <rect width="700" height="400" fill="url(#copperBack)"/>
    <ellipse cx="330" cy="170" rx="440" ry="265" fill="url(#skyBack)"/>
  </svg>
  <div class="appt">
    <div class="appt__rule"></div>
    <h2 class="appt__title">Has An Appoinment On</h2>
    <ul class="days">
      <li class="day"><span class="day__box"></span>Mon</li>
      <li class="day"><span class="day__box"></span>Tues</li>
      <li class="day"><span class="day__box"></span>Wed</li>
      <li class="day"><span class="day__box"></span>Thur</li>
      <li class="day"><span class="day__box"></span>Fri</li>
      <li class="day"><span class="day__box"></span>Sat</li>
    </ul>
    <div class="when">
      <span>Date</span>
      <span class="when__line when__line--date"></span>
      <span>AT</span>
      <span class="when__line"></span>
      <span class="when__meridiem">am.<br>pm.</span>
    </div>
    <p class="appt__web">www.brightpathwellclinic.example</p>
  </div>
</section>

</body>
</html>
```